Bref créative
PRDL
Stationary & Business Cards
I need double sided standard sized Business Card [3.5" x 2"]
non specific
Modern
Pine Ridge Dragster League
www.prdlmotors-example.com
info@prdlmotors-example.com
The Pine Ridge Dragster League showcases the best of heads up and index drag racing for racers, fans and families!
Visit the PRDL website for more information & race dates.

```html
<!DOCTYPE html>
<html lang="en">
<head>
<meta charset="utf-8">
<title>Pine Ridge Dragster League – Business Card</title>
<link href="https://fonts.googleapis.com/css2?family=Arimo:wght@400;700&display=swap" rel="stylesheet">
<style>
  :root {
    --stage: #1e1e1f;
    --card-black: #050505;
    --card-white: #ffffff;
    --silver-light: #f2f2f2;
    --silver-dark: #8a8a8a;
    --text-light: #ffffff;
    --text-dark: #2a2a2a;
    --accent-red: #d3201c;
  }
  html, body {
    margin: 0;
    padding: 0;
    overflow: hidden;
  }
  .stage {
    position: relative;
    width: 1200px;
    height: 883px;
    background: var(--stage);
    font-family: "Arimo", Arial, sans-serif;
    overflow: hidden;
  }
  .card {
    position: absolute;
    border-radius: 24px;
    overflow: hidden;
  }
  .card-front {
    left: 132px;
    top: 96px;
    width: 600px;
    height: 343px;
  }
  .card-front .card-shapes {
    position: absolute;
    inset: 0;
  }
  .league-title {
    position: absolute;
    left: 348px;
    top: 28px;
    margin: 0;
    color: var(--text-light);
    font-size: 12px;
    font-weight: 400;
    letter-spacing: 0.5px;
    text-transform: uppercase;
  }
  .brand-name {
    position: absolute;
    left: 42px;
    top: 180px;
    margin: 0;
    color: var(--accent-red);
    font-size: 58px;
    font-weight: 700;
    letter-spacing: 2px;
    line-height: 1;
  }
  .contact {
    position: absolute;
    bottom: 12px;
    margin: 0;
    color: var(--text-light);
    font-size: 11px;
    letter-spacing: 1.2px;
    text-transform: uppercase;
  }
  .contact-email { left: 26px; }
  .contact-web { right: 24px; }

  .card-back {
    left: 473px;
    top: 463px;
    width: 607px;
    height: 353px;
    background: var(--card-black);
  }
  .back-message {
    position: absolute;
    left: 90px;
    right: 90px;
    top: 145px;
    margin: 0;
    color: var(--text-light);
    font-size: 12.5px;
    line-height: 1.55;
    letter-spacing: 0.2px;
    text-transform: uppercase;
  }
  .back-message .highlight { color: var(--accent-red); }
  .bolt {
    position: absolute;
    top: 158px;
    width: 30px;
    height: 30px;
  }
  .bolt-left { left: 36px; }
  .bolt-right { right: 36px; }
</style>
</head>
<body>
<main class="stage">

  <section class="card card-front" aria-label="Business card front">
    <svg class="card-shapes" width="600" height="343" viewBox="0 0 600 343" aria-hidden="true">
      <defs>
        <linearGradient id="swoosh" x1="0" y1="0" x2="1" y2="0">
          <stop offset="0" stop-color="var(--silver-light)"/>
          <stop offset="0.55" stop-color="var(--silver-dark)"/>
          <stop offset="1" stop-color="var(--silver-light)"/>
        </linearGradient>
      </defs>
      <rect width="600" height="343" fill="var(--card-black)"/>
      <path d="M0 80 C180 64 420 140 600 300 L600 312 L0 312 Z" fill="var(--card-white)"/>
      <path d="M150 72 C320 82 470 170 600 292" fill="none" stroke="url(#swoosh)" stroke-width="9"/>
    </svg>
    <h1 class="league-title">Pine Ridge Dragster League</h1>
    <p class="brand-name">PRDL</p>
    <p class="contact contact-email">info@prdlmotors-example.com</p>
    <p class="contact contact-web">www.prdlmotors-example.com</p>
  </section>

  <section class="card card-back" aria-label="Business card back">
    <svg class="bolt bolt-left" viewBox="0 0 30 30" aria-hidden="true">
      <circle cx="15" cy="15" r="14" fill="var(--silver-dark)" stroke="var(--silver-light)" stroke-width="2"/>
      <rect x="4" y="13" width="22" height="4" fill="var(--card-black)"/>
    </svg>
    <p class="back-message">
      The Pine Ridge Dragster League showcases the best of heads up and index drag racing for racers, fans and families!
      Visit the <span class="highlight">PRDL</span> website for more information &amp; race dates.
    </p>
    <svg class="bolt bolt-right" viewBox="0 0 30 30" aria-hidden="true">
      <circle cx="15" cy="15" r="14" fill="var(--silver-dark)" stroke="var(--silver-light)" stroke-width="2"/>
      <rect x="4" y="13" width="22" height="4" fill="var(--card-black)"/>
    </svg>
  </section>

</main>
</body>
</html>
```